Something that stands out and has more of a modern look to it...will be printing on plastic cards so keep in mind and review old business card as reference

Industry/Entity Type

Real Estate Agent

Contact Information for Business Card

Front of business card will have picture and information the back of card can have logo or name in cursive etc

Logo Text

Marcus Belvane

Font styles to use
Decorative
Script

Colors

Designer to choose colors to be used in the design.

Requirements
Must have
• Must have "Harborline 47" logo and state "Quiet Summit Realty Inc Brokerage*" next to it.
• Offices in: Toronto, Markham, Durham
• *Independently Owned and Operated trademarks owned by Harborline 47 Real Estate LLC used under license or authorized sub-license. 2017 Harborline 47 Canada Limited Partnership. (See old business card for reference)
• Email address: marcus@mbelvanehomes.example
• Website: www.MBelvaneHomes.example
• Direct: 647-555-0143
• Name: Marcus Bel Vane
• Office: 905-555-0178
Nice to have
• Maybe a catchy slogan
• One side can have my name designed or the Logo
Should not have
• The Harborline 47 Logo too large or focused on (my business requires me just to have this somewhere on the card).
• Yellow and black theme

```html
<!DOCTYPE html>
<html lang="en">
<head>
<meta charset="utf-8">
<title>M Belvane Realty – Business Card</title>
<link href="https://fonts.googleapis.com/css2?family=Montserrat:wght@700&family=Open+Sans:wght@400;600&display=swap" rel="stylesheet">
<style>
  :root {
    --brand-red: #e30d10;
    --navy: #143159;
    --ink: #2b2b2b;
    --paper: #ffffff;
    --backdrop: #ecebe8;
  }
  * { box-sizing: border-box; margin: 0; padding: 0; }
  html, body { width: 1200px; height: 900px; overflow: hidden; }
  body {
    background: var(--backdrop);
    font-family: "Open Sans", Arial, sans-serif;
    display: flex;
    align-items: center;
    justify-content: center;
    gap: 40px;
  }
  .card {
    position: relative;
    width: 540px;
    height: 310px;
    overflow: hidden;
    box-shadow: 0 10px 24px rgba(0,0,0,.18);
  }
  .card--back {
    background: var(--brand-red);
    display: flex;
    align-items: center;
    justify-content: center;
  }
  .wordmark {
    font-family: "Montserrat", Arial, sans-serif;
    font-weight: 700;
    letter-spacing: .5px;
    white-space: nowrap;
  }
  .card--back .wordmark { color: var(--paper); font-size: 34px; }
  .card--front { background: var(--paper); }
  .card--front .wordmark {
    position: absolute;
    top: 28px; right: 28px;
    color: var(--brand-red);
    font-size: 25px;
  }
  .wave { position: absolute; inset: 0; }
  .portrait {
    position: absolute;
    left: 92px; top: 112px;
    width: 200px; height: 198px;
    border-radius: 90px 90px 0 0;
    background: linear-gradient(180deg, #b98d74 0%, #8a6a5a 38%, #1f4f8e 60%, #173b6b 100%);
  }
  .contact {
    position: absolute;
    top: 70px; right: 30px;
    text-align: right;
    color: var(--ink);
  }
  .contact__name {
    font-family: "Montserrat", Arial, sans-serif;
    font-weight: 700;
    color: var(--brand-red);
    font-size: 15px;
    letter-spacing: .5px;
  }
  .contact__role { font-size: 10.5px; margin-bottom: 8px; }
  .contact__line {
    display: flex;
    justify-content: flex-end;
    align-items: center;
    gap: 6px;
    font-size: 11px;
    line-height: 17px;
  }
  .contact__label { color: var(--brand-red); font-weight: 600; }
  .icon { width: 9px; height: 9px; fill: var(--brand-red); }
  .brokerage {
    position: absolute;
    right: 28px; top: 228px;
    color: var(--paper);
    text-align: right;
    font-size: 9.5px;
    line-height: 14px;
  }
  .brokerage__mark {
    display: inline-flex;
    align-items: center;
    gap: 5px;
    font-weight: 600;
    font-size: 10.5px;
  }
  .brokerage__mark::before {
    content: "";
    width: 7px; height: 7px;
    background: var(--paper);
  }
  .disclaimer {
    position: absolute;
    right: 28px; top: 276px;
    width: 220px;
    color: rgba(255,255,255,.85);
    text-align: right;
    font-size: 6px;
    line-height: 8px;
  }
</style>
</head>
<body>
  <section class="card card--back">
    <span class="wordmark">M BELVANE REALTY</span>
  </section>

  <section class="card card--front">
    <span class="wordmark">M BELVANE REALTY</span>

    <div class="portrait" role="img" aria-label="Portrait photo of the agent in a navy blazer and white shirt"></div>

    <svg class="wave" viewBox="0 0 540 310" aria-hidden="true">
      <path d="M0 278 C140 302 290 262 390 228 C455 206 505 198 540 198 L540 310 L0 310 Z" fill="var(--navy)"/>
    </svg>

    <div class="contact">
      <div class="contact__name">MARCUS BEL VANE</div>
      <div class="contact__role">Sales Representative</div>
      <div class="contact__line"><span class="contact__label">D</span> 647-555-0143
        <svg class="icon" viewBox="0 0 10 10"><path d="M2 0.5 L4 3 L3 4 C3.6 5.4 4.6 6.4 6 7 L7 6 L9.5 8 L8.5 9.5 C4 9.5 0.5 6 0.5 1.5 Z"/></svg>
      </div>
      <div class="contact__line"><span class="contact__label">O</span> 905-555-0178
        <svg class="icon" viewBox="0 0 10 10"><path d="M2 0.5 L4 3 L3 4 C3.6 5.4 4.6 6.4 6 7 L7 6 L9.5 8 L8.5 9.5 C4 9.5 0.5 6 0.5 1.5 Z"/></svg>
      </div>
      <div class="contact__line">marcus@mbelvanehomes.example
        <svg class="icon" viewBox="0 0 10 10"><rect x="0.5" y="2" width="9" height="6.5" rx="0.8"/><path d="M0.8 2.4 L5 5.6 L9.2 2.4" stroke="#fff" stroke-width="0.9" fill="none"/></svg>
      </div>
      <div class="contact__line">www.MBelvaneHomes.example
        <svg class="icon" viewBox="0 0 10 10"><circle cx="5" cy="5" r="4.5"/><path d="M0.5 5 H9.5 M5 0.5 C3 3 3 7 5 9.5 M5 0.5 C7 3 7 7 5 9.5" stroke="#fff" stroke-width="0.7" fill="none"/></svg>
      </div>
    </div>

    <div class="brokerage">
      <div class="brokerage__mark">Harborline 47</div>
      <div>Quiet Summit Realty Inc Brokerage*</div>
      <div>Offices: Toronto · Markham · Durham</div>
    </div>

    <p class="disclaimer">*Independently Owned and Operated trademarks owned by Harborline 47 Real Estate LLC used under license or authorized sub-license. 2017 Harborline 47 Canada Limited Partnership.</p>
  </section>
</body>
</html>
```